Moving Postcard

I need a postcard to let people know my law firm is moving effective Jan 1 2018 to Harlow Tower Suite 2700 2836 Larkmoor Street Seattle Washington 98127-3460. A copy of my current letterhead, business card, and envelope (all of which I like) are attached. The color is odd on the scan but it's a dark purple or purplish-brown. I was to keep the 'focused, fearless defense' (but drop the criminal) and perhaps specify elsewhere I'm talking about criminal defense, lawyer discipline defense, and judicial conduct defense. I'd like a design I can easily upload and have printed by Zint

Law Firm

```html
<!DOCTYPE html>
<html lang="en">
<head>
<meta charset="utf-8">
<title>Dana Whitlock – Moving Postcard</title>
<link href="https://fonts.googleapis.com/css2?family=Oswald:wght@400;500&family=EB+Garamond:wght@400;500&family=Libre+Baskerville:wght@700&family=Cinzel:wght@500&display=swap" rel="stylesheet">
<style>
  :root{
    --plum:#3a2a3e;
    --brown:#4f2b14;
    --cream:#f1ece0;
    --ink:#2b2528;
    --paper:#ffffff;
    --backdrop:#d6d6d6;
    --rule:#9a8f9c;
  }
  *{box-sizing:border-box;margin:0;padding:0}
  html,body{width:1200px;height:1200px;overflow:hidden;background:var(--backdrop)}
  .card{position:absolute;width:678px;height:525px;background:var(--paper);overflow:hidden;box-shadow:0 3px 10px rgba(0,0,0,.25)}
  .front{left:136px;top:54px}
  .back{left:399px;top:601px}
  .shapes{position:absolute;left:0;top:0}
  .abs{position:absolute}

  /* front */
  .headline{left:24px;top:18px;color:#fff}
  .headline-caps{font:500 39px/1 "Oswald",sans-serif;letter-spacing:-.3px}
  .headline-script{font:700 31px/1.32 "Libre Baskerville",serif;margin-top:4px}
  .brand{right:38px;top:72px;text-align:center;color:#fff}
  .brand-name{font:400 37px/1 "Oswald",sans-serif;letter-spacing:.5px}
  .brand-tag{font:400 12px/1 "EB Garamond",serif;margin-top:6px}
  .portrait{left:18px;top:179px;width:238px;height:238px;border-radius:50%;border:2px solid var(--plum);padding:6px}
  .portrait-fill{width:100%;height:100%;border-radius:50%;background:radial-gradient(circle at 50% 45%,#b07a52 0%,#7a4a34 45%,#2e2326 100%)}
  .attorney{left:0;width:274px;top:430px;text-align:center}
  .attorney-name{font:500 25px/1 "Cinzel",serif;color:var(--brown)}
  .attorney-title{font:400 15px/1 "EB Garamond",serif;color:var(--ink);margin-top:6px}
  .bio{left:275px;top:190px;width:381px;font:400 14px/18.4px "EB Garamond",serif;color:var(--ink);text-align:justify}
  .section-title{left:275px;top:306px;font:400 19px/1 "Oswald",sans-serif;color:var(--plum);letter-spacing:-.3px}
  .dots{border-bottom:2px dotted var(--rule)}
  .practice-rule{left:275px;top:332px;width:192px}
  .practice{left:275px;top:340px;width:390px;display:grid;grid-template-columns:195px 195px;row-gap:5px;font:400 16px/19px "EB Garamond",serif;color:var(--ink)}
  .practice li{list-style:none;display:flex;align-items:center;gap:4px}
  .tick{width:10px;height:10px;flex:none}
  .call{left:275px;top:446px;font:400 19px/1 "Oswald",sans-serif;color:var(--plum);letter-spacing:-.3px}
  .call b{font:500 21px/1 "EB Garamond",serif;color:var(--brown)}
  .call-rule{left:275px;top:474px;width:305px}
  .site-band{left:0;bottom:0;width:100%;height:36px;background:var(--plum);color:#fff;text-align:center;font:400 15px/36px "EB Garamond",serif;letter-spacing:3.4px}

  /* back */
  .testimonials{left:0;top:20px;width:370px;text-align:center;color:var(--ink);font:400 13.4px/15.6px "EB Garamond",serif}
  .quote{padding:0 24px}
  .quote-rule{width:232px;margin:4px auto 13px}
  .back-brand{left:27px;top:219px}
  .back-brand .brand-name{font:500 33px/1 "Oswald",sans-serif;color:var(--ink)}
  .back-brand .brand-tag{font:400 12px/1 "EB Garamond",serif;color:var(--ink);margin-top:6px;padding-left:8px}
  .gavel{left:257px;top:210px;width:113px;height:106px;background:linear-gradient(160deg,var(--cream) 0%,#c9a27e 55%,#6a3c22 100%)}
  .moving{left:27px;top:317px;width:311px;color:#fff;text-align:center}
  .moving-title{font:400 19px/1 "Oswald",sans-serif;letter-spacing:-.3px;position:relative;z-index:1;display:inline-block;padding:0 10px;background:var(--plum)}
  .moving-box{border:1.5px solid #fff;margin-top:-10px;padding:12px 6px 8px;font:700 14px/18px "Libre Baskerville",serif;font-family:"EB Garamond",serif;font-weight:500;font-size:16px}
  .moving-zip{font:500 25px/1 "EB Garamond",serif;margin-top:6px}
  .effective{left:0;width:370px;top:414px;text-align:center;color:#fff}
  .effective-label{font:400 12px/1 "EB Garamond",serif}
  .effective-date{font:400 34px/1 "Oswald",sans-serif;margin-top:4px;letter-spacing:-.5px}
  .back-site{left:0;width:370px;top:497px;text-align:center;color:#fff;font:400 13px/1 "EB Garamond",serif;letter-spacing:2.8px}
  .stamp{left:603px;top:18px;width:58px;height:65px;border:1px solid #777}
  .address-line{left:489px;width:166px;border-top:1px solid #999}
  .badge{top:478px}
</style>
</head>
<body>

<section class="card front" aria-label="Postcard front">
  <svg class="shapes" width="678" height="525" viewBox="0 0 678 525" aria-hidden="true">
    <polygon points="0,0 630,0 320,100 0,202" fill="var(--plum)"/>
    <polygon points="610,0 678,0 678,184 320,100" fill="var(--brown)"/>
  </svg>
  <div class="abs headline">
    <div class="headline-caps">FOCUSED, FEARLESS DEFENSE</div>
    <div class="headline-script">when you need<br>it most!!</div>
  </div>
  <div class="abs brand">
    <div class="brand-name">DANA WHITLOCK</div>
    <div class="brand-tag">focused, fearless criminal defense</div>
  </div>
  <div class="abs portrait"><div class="portrait-fill" role="img" aria-label="Portrait photograph of the attorney"></div></div>
  <div class="abs attorney">
    <div class="attorney-name">DANA WHITLOCK</div>
    <div class="attorney-title">Attorney at Law</div>
  </div>
  <p class="abs bio">Dana Whitlock is a fearless criminal defense attorney intensely devoted to advocating on behalf of individuals accused of committing serious crimes in Washington state. Ms. Whitlock has built an incredibly strong background in criminal trial and appellate practice and has been recognized repeatedly for her acumen in these areas.</p>
  <div class="abs section-title">PRACTICE AREAS</div>
  <div class="abs dots practice-rule"></div>
  <ul class="abs practice">
    <li><svg class="tick" viewBox="0 0 10 10"><rect x=".5" y="2" width="7" height="7" fill="none" stroke="#444" stroke-width=".9"/><path d="M2 5l2 2 5-6" fill="none" stroke="#444" stroke-width="1.2"/></svg>Sex offenses</li>
    <li><svg class="tick" viewBox="0 0 10 10"><rect x=".5" y="2" width="7" height="7" fill="none" stroke="#444" stroke-width=".9"/><path d="M2 5l2 2 5-6" fill="none" stroke="#444" stroke-width="1.2"/></svg>Criminal defense</li>
    <li><svg class="tick" viewBox="0 0 10 10"><rect x=".5" y="2" width="7" height="7" fill="none" stroke="#444" stroke-width=".9"/><path d="M2 5l2 2 5-6" fill="none" stroke="#444" stroke-width="1.2"/></svg>Violent crimes</li>
    <li><svg class="tick" viewBox="0 0 10 10"><rect x=".5" y="2" width="7" height="7" fill="none" stroke="#444" stroke-width=".9"/><path d="M2 5l2 2 5-6" fill="none" stroke="#444" stroke-width="1.2"/></svg>Lawyer discipline defense</li>
    <li><svg class="tick" viewBox="0 0 10 10"><rect x=".5" y="2" width="7" height="7" fill="none" stroke="#444" stroke-width=".9"/><path d="M2 5l2 2 5-6" fill="none" stroke="#444" stroke-width="1.2"/></svg>Property and drug crimes</li>
    <li><svg class="tick" viewBox="0 0 10 10"><rect x=".5" y="2" width="7" height="7" fill="none" stroke="#444" stroke-width=".9"/><path d="M2 5l2 2 5-6" fill="none" stroke="#444" stroke-width="1.2"/></svg>Judicial conduct defense</li>
    <li><svg class="tick" viewBox="0 0 10 10"><rect x=".5" y="2" width="7" height="7" fill="none" stroke="#444" stroke-width=".9"/><path d="M2 5l2 2 5-6" fill="none" stroke="#444" stroke-width="1.2"/></svg>Disciplinary actions</li>
  </ul>
  <div class="abs call">CALL US NOW : <b>(206) 555-0183</b></div>
  <div class="abs dots call-rule"></div>
  <div class="abs site-band">www.whitlockdefense.com</div>
</section>

<section class="card back" aria-label="Postcard back">
  <svg class="shapes" width="678" height="525" viewBox="0 0 678 525" aria-hidden="true">
    <rect x="0" y="0" width="370" height="525" fill="var(--cream)"/>
    <polygon points="0,275 370,311 370,525 0,525" fill="var(--plum)"/>
    <polygon points="0,492 370,470 370,525 0,525" fill="var(--brown)"/>
    <line x1="0" y1="490" x2="370" y2="468" stroke="#fff" stroke-width="1.5"/>
  </svg>
  <div class="abs testimonials">
    <p class="quote">"Thank you again for helping our son.<br>We often think of you and how blessed we were to have you on our side."</p>
    <div class="dots quote-rule"></div>
    <p class="quote">"I can't put into words how amazing it feels knowing I will be able to live a normal life thanks to you. I'll never forget what you have done for me."</p>
    <div class="dots quote-rule"></div>
    <p class="quote">"I just wanted to thank you again. I've finished going through my file and now I'm completely aware of the effort you put into my case."</p>
    <div class="dots quote-rule"></div>
  </div>
  <div class="abs gavel" role="img" aria-label="Photograph of a wooden gavel"></div>
  <div class="abs back-brand">
    <div class="brand-name">DANA WHITLOCK</div>
    <div class="brand-tag">focused, fearless criminal defense</div>
  </div>
  <div class="abs moving">
    <div class="moving-title">We are now moving to</div>
    <div class="moving-box">
      Harlow Tower Suite 2700 2836 Larkmoor<br>Street Seattle Washington
      <div class="moving-zip">98127-3460</div>
    </div>
  </div>
  <div class="abs effective">
    <div class="effective-label">Effective</div>
    <div class="effective-date">01.01. 2018</div>
  </div>
  <div class="abs back-site">www.whitlockdefense.com</div>

  <div class="abs stamp" aria-label="Stamp area"></div>
  <div class="abs address-line" style="top:226px"></div>
  <div class="abs address-line" style="top:252px"></div>
  <div class="abs address-line" style="top:278px"></div>

  <svg class="abs badge" style="left:385px" width="36" height="28" aria-hidden="true"><rect x="1" y="1" width="34" height="26" rx="2" fill="#fff" stroke="#999"/></svg>
  <svg class="abs badge" style="left:444px" width="36" height="34" aria-hidden="true"><circle cx="18" cy="16" r="15" fill="#fff" stroke="#1f3e8a" stroke-width="3"/></svg>
  <svg class="abs badge" style="left:507px" width="36" height="34" aria-hidden="true"><circle cx="18" cy="16" r="15" fill="#fff" stroke="#1f3e8a" stroke-width="3"/></svg>
  <svg class="abs badge" style="left:575px" width="46" height="28" aria-hidden="true"><rect x="1" y="4" width="12" height="20" fill="#c9a54a"/></svg>
</section>

</body>
</html>
```